Global Weight loss program

we need a business card based in Brooklyn , NY called PeppertonRUN . Mara Dulvik Tenbrook the founder and creator of PeppertonRUN Movement. A business based around nutrition, health, Whole Foods and fitness.

Industry/Entity Type

Food Service

Contact Information for Business Card

Phone number : 718-555-0143
website www.peppertonrun.com
email : mara@peppertonrun.com

Font styles to use
Sans Serif

Requirements
Must have
• logo colors
• green black and gold
Nice to have
• must be simple and sharp.
Should not have
• pictures of items

```html
<!DOCTYPE html>
<html lang="en">
<head>
<meta charset="utf-8">
<title>PeppertonRUN Business Card</title>
<link rel="stylesheet" href="https://fonts.googleapis.com/css2?family=Lato:wght@400;700&family=Raleway:wght@400&family=Ubuntu:wght@500&display=swap">
<style>
  :root {
    --page-bg: #1b1b1b;
    --card-white: #ffffff;
    --ink-dark: #333333;
    --ink-mid: #555555;
    --ink-soft: #777777;
    --brand-green: #6db33f;
    --green-deep: #3f8a3a;
    --green-bright: #9ccc3c;
    --frame-light: #ffffff;
  }
  * { margin: 0; padding: 0; box-sizing: border-box; }
  html, body {
    width: 1200px; height: 897px; overflow: hidden;
    background: var(--page-bg);
  }
  .canvas { position: relative; width: 1200px; height: 897px; }
  .card {
    position: absolute; left: 303px; width: 595px; height: 339px;
    text-align: center;
  }
  .card-front { top: 92px; background: var(--card-white); }
  .card-back {
    top: 469px;
    background: linear-gradient(100deg, var(--green-deep) 0%, #5aa63f 30%, #7fbf3e 65%, var(--green-bright) 100%);
  }
  .card-frame {
    position: absolute; inset: 21px;
    border: 1px solid var(--brand-green);
  }
  .card-back .card-frame { border-color: var(--frame-light); }
  .brand-mark {
    position: absolute; left: 50%; transform: translateX(-50%);
  }
  .card-front .brand-mark {
    top: 72px; width: 78px; height: 78px; background: var(--brand-green);
  }
  .card-back .brand-mark {
    top: 80px; width: 100px; height: 100px; background: var(--frame-light);
  }
  .brand-name {
    position: absolute; left: 0; right: 0;
    font-family: "Ubuntu", sans-serif; font-weight: 500;
    letter-spacing: -0.5px;
  }
  .card-front .brand-name { top: 168px; font-size: 37px; color: var(--ink-dark); }
  .card-back .brand-name { top: 199px; font-size: 45px; color: var(--frame-light); }
  .brand-tagline {
    position: absolute; left: 0; right: 0;
    font-family: "Lato", sans-serif; letter-spacing: 2.2px;
  }
  .card-front .brand-tagline { top: 210px; font-size: 9.5px; color: var(--ink-soft); }
  .card-back .brand-tagline { top: 250px; font-size: 11px; color: rgba(255,255,255,0.85); }
  .person-line {
    position: absolute; top: 237px; left: 0; right: 0;
    font-family: "Lato", sans-serif; letter-spacing: 1px;
  }
  .person-name { font-size: 19px; color: var(--brand-green); }
  .person-role { font-size: 15px; color: var(--ink-dark); }
  .contact-line {
    position: absolute; top: 267px; left: 0; right: 0;
    font-family: "Lato", sans-serif; font-size: 13.5px; color: var(--ink-mid);
    white-space: nowrap;
  }
  .contact-label, .contact-sep, .contact-accent { color: var(--brand-green); }
  .back-url {
    position: absolute; top: 287px; left: 0; right: 0;
    font-family: "Raleway", sans-serif; font-size: 16.5px; letter-spacing: 2px;
    color: var(--frame-light);
  }
</style>
</head>
<body>
<main class="canvas">
  <section class="card card-front" aria-label="Business card front">
    <div class="card-frame"></div>
    <div class="brand-mark"></div>
    <div class="brand-name">PeppertonRUN</div>
    <div class="brand-tagline">Fitness, Nutrition and Health</div>
    <div class="person-line">
      <span class="person-name">MARA TENBROOK -</span>
      <span class="person-role">FOUNDER</span>
    </div>
    <div class="contact-line">
      <span class="contact-label">Cell:</span> 718-555-0143
      <span class="contact-sep">|</span>
      <span class="contact-label">Email:</span> mara@peppertonrun.com
      <span class="contact-sep">|</span>
      <span class="contact-label">Web:</span> www.<span class="contact-accent">peppertonrun</span>.com
    </div>
  </section>

  <section class="card card-back" aria-label="Business card back">
    <div class="card-frame"></div>
    <div class="brand-mark"></div>
    <div class="brand-name">PeppertonRUN</div>
    <div class="brand-tagline">Fitness, Nutrition and Health</div>
    <div class="back-url">www.peppertonrun.com</div>
  </section>
</main>
</body>
</html>
```